Webdesign für Immobilienmakler / Immobilienbüro
Zielgruppe
Das Unternehmen heißt LUMAR GmbH und kommt aus Heerbrugg in der Schweiz und will nun den Bereich Immobilien Vermarktung, Verkauf, Vermietung auf Süddeutschland erweitern.
Wir haben bis heute keine Webseite, weil unser Geschäft bis dato in der Schweiz durch Empfehlung, Mundpropaganda und Zeitunganzeigen funktioniert hat. Aber in Deutschland ist es ja ein Muß, was uns sicherlich auch den Einstieg erleichtern wird.
Aufgabenstellung
Wir benötigen eine Homepage für den Verkauf, Vermietung, Vermittlung von Immobilien für Privat und Gewerbe. Zu den Kategorien und der Gliederung haben wir keine bestimmte Vorstellung.
Hier hat der Designer freie Hand und wir freuen uns auf Ihren Vorschlag

```html
<!DOCTYPE html>
<html lang="de">
<head>
<meta charset="utf-8">
<title>LUMAR GmbH – Immobilien</title>
<link rel="stylesheet" href="https://fonts.googleapis.com/css2?family=Arimo:wght@400;700&family=Source+Serif+4:ital,wght@1,400;1,600&display=swap">
<style>
:root{
  --green:#5aab0a;
  --green-dark:#4a9105;
  --dark:#3a3a3a;
  --darker:#2e2e2e;
  --text:#333;
  --muted:#777;
  --line:#ddd;
  --page:#f5f5f5;
  --white:#fff;
}
*{box-sizing:border-box;margin:0;padding:0}
html,body{width:782px;height:1200px;overflow:hidden;background:var(--page)}
body{font-family:"Arimo",Helvetica,Arial,sans-serif;color:var(--text)}
.page{width:1280px;height:1965px;transform:scale(.6109);transform-origin:0 0;position:relative;background:var(--page)}
.abs{position:absolute}
.serif{font-family:"Source Serif 4",Georgia,serif;font-style:italic}

/* top bar */
.topbar{left:0;top:0;width:1280px;height:40px;background:var(--dark)}
.topbar .home{left:70px;top:0;width:47px;height:40px;background:#f0f0f0;display:flex;align-items:center;justify-content:center}
.nav{left:120px;top:0;height:40px;display:flex}
.nav a{color:#ccc;text-decoration:none;font-size:13px;font-weight:700;letter-spacing:.2px;padding:0 16px;line-height:40px;border-right:1px solid #2a2a2a}
.social{right:70px;top:12px;display:flex;gap:10px}
.social span{width:16px;height:16px;background:#777;border-radius:2px}

/* header */
.header{left:0;top:40px;width:1280px;height:70px;background:var(--white)}
.brand{left:68px;top:14px;font-size:36px;font-weight:700;color:var(--text);letter-spacing:.5px}
.slogan{left:228px;top:22px;height:28px;border-left:1px solid #ccc;padding-left:14px;line-height:32px;font-size:12px;letter-spacing:1.2px;color:#555}
.service{right:95px;top:22px;font-size:24px;color:var(--text);letter-spacing:-.5px;display:flex;align-items:center;gap:10px}
.service b{font-weight:700}

/* hero */
.hero{left:0;top:110px;width:1280px;height:400px;background:linear-gradient(90deg,#7e9a5c 0%,#c9d4c4 12%,#e4e8ea 40%,#dfe5e8 70%,#8ea36f 100%)}
.hero-panel{left:70px;top:140px;width:1140px;height:338px;background:rgba(255,255,255,.72)}
.hero h1{left:98px;top:192px;font-size:58px;font-weight:700;letter-spacing:-2px;color:#222}
.hero-lead{left:98px;top:272px;width:680px;font-size:23px;line-height:30px;color:#222}
.btn{background:var(--green);color:var(--white);font-weight:700;border:1px solid var(--green-dark);display:flex;align-items:center;justify-content:center}
.hero .btn-offers{left:98px;top:356px;width:235px;height:35px;font-size:16px}
.search-title{left:886px;top:167px;font-size:17px;color:#222}
.select{height:23px;background:#f7f7f7;border:1px solid #aaa;border-radius:3px;font-size:12px;color:#333;padding-left:8px;line-height:21px}
.select::after{content:"";position:absolute;right:8px;top:5px;width:0;height:0;border:3px solid transparent;border-bottom:4px solid #333;border-top:none}
.select::before{content:"";position:absolute;right:8px;top:12px;width:0;height:0;border:3px solid transparent;border-top:4px solid #333;border-bottom:none}
.btn-search{left:1043px;top:412px;width:135px;height:35px;font-size:16px}

/* listings */
.section-title{font-size:19px;color:#333}
.all{left:1084px;top:531px;font-size:14px;color:var(--green)}
.arrows{left:1160px;top:527px;display:flex;gap:2px}
.arrows span{width:23px;height:23px;background:#222;display:flex;align-items:center;justify-content:center}
.card{top:569px;width:350px;height:346px;background:var(--white);box-shadow:0 1px 2px rgba(0,0,0,.08)}
.card .photo{position:absolute;left:0;top:0;width:350px;height:200px}
.card .tag{position:absolute;left:0;top:0;height:32px;padding:0 12px;background:#222;color:#fff;font-size:14px;line-height:32px}
.card .addr{position:absolute;left:23px;top:214px;font-size:17px;color:#222}
.card .row{position:absolute;left:19px;width:302px;height:30px;border-bottom:1px dotted #ccc;font-size:13px}
.card .row b{position:absolute;left:0;top:8px}
.card .row i{position:absolute;right:0;font-style:normal;color:#888}

/* call to action */
.cta{left:70px;top:940px;width:1141px;height:95px;background:var(--white);box-shadow:0 1px 2px rgba(0,0,0,.08)}
.cta .headline{position:absolute;left:32px;top:27px;font-size:19px;color:#222}
.cta .sub{position:absolute;left:32px;top:52px;font-size:13px;color:#777}
.cta .btn{position:absolute;left:913px;top:26px;width:199px;height:45px;font-size:18px}

/* team */
.member{top:1090px}
.member .photo{width:155px;height:153px;border:2px solid #fff;box-shadow:0 1px 2px rgba(0,0,0,.1)}
.member .name{margin-top:26px;font-size:13px;color:#666}
.member .link{font-size:14px;color:var(--green);margin-top:2px}
.bullets{left:850px;top:1083px;list-style:none}
.bullets li{font-size:14px;color:#666;line-height:24px;padding-left:16px;position:relative}
.bullets li::before,.foot-links li::before{content:"›";position:absolute;left:0;color:#999}

/* footer */
.footer{left:0;top:1322px;width:1280px;height:298px;background:var(--dark);color:#bbb}
.foot-brand{left:68px;top:30px;font-size:30px;font-weight:700;color:#fff;letter-spacing:-.5px}
.foot-slogan{left:70px;top:69px;font-size:12px;letter-spacing:1.5px;color:#ddd}
.foot-text{left:70px;top:100px;width:250px;font-size:13px;line-height:18px;color:#999}
.foot-head{top:34px;width:252px;padding-bottom:16px;border-bottom:1px solid #4d4d4d;font-size:17px;color:#eee}
.foot-addr{left:366px;top:88px;font-size:13px;line-height:18px;color:#aaa}
.foot-addr div{position:relative;padding-left:26px;margin-bottom:7px}
.foot-addr svg{position:absolute;left:0;top:2px}
.foot-links{left:661px;top:86px;list-style:none}
.foot-links li{font-size:13px;color:#aaa;line-height:24px;padding-left:15px;position:relative}
.foot-photo{left:952px;top:91px;width:265px;height:165px;background:linear-gradient(180deg,#4c7fc2 0%,#8fb3d9 40%,#c84b3c 55%,#e9e9e9 65%,#5f8f33 85%,#4a7a28 100%)}
</style>
</head>
<body>
<div class="page">

  <div class="abs topbar">
    <div class="abs home">
      <svg width="16" height="14" viewBox="0 0 16 14"><path d="M8 0 0 7h2v7h4V9h4v5h4V7h2z" fill="#333"/></svg>
    </div>
    <nav class="abs nav">
      <a>ÜBER UNS</a><a>VERMIETUNG</a><a>VERKAUF</a><a>VERKAUF</a><a>PHILOSOPHIE</a><a>KONTAKT</a>
    </nav>
    <div class="abs social" aria-label="Soziale Netzwerke"><span></span><span></span><span></span><span></span></div>
  </div>

  <header class="abs header">
    <div class="abs brand">LUMAR</div>
    <div class="abs slogan">IHR SLOGAN KOMMT HIERHIN</div>
    <div class="abs service">
      <svg width="14" height="18" viewBox="0 0 14 18"><path d="M3 0 0 2c0 9 5 15 11 16l3-3-3-4-3 2c-2-2-3-4-3-7l3-1z" fill="#333"/></svg>
      <span>Serviceline: <b>0170 5566 820</b></span>
    </div>
  </header>

  <section class="abs hero" role="img" aria-label="Foto eines weißen Mehrfamilienhauses mit Bäumen"></section>
  <div class="abs hero-panel"></div>
  <div class="hero">
    <h1 class="abs">Willkommen bei LUMAR!</h1>
    <p class="abs hero-lead">Lorem ipsum dolor sit amet consectetur incididunt ut labore et dolore magna aliqua adipisicing elit seddo eiusmod tempor.</p>
    <div class="abs btn btn-offers">Unsere Angebote</div>
  </div>

  <div class="abs search-title">FINDEN SIE IHR ZUHAUSE!</div>
  <div class="abs select" style="left:887px;top:202px;width:292px">Haustyp</div>
  <div class="abs select" style="left:887px;top:242px;width:135px">Zimmer</div>
  <div class="abs select" style="left:1044px;top:242px;width:135px">Bäder</div>
  <div class="abs select" style="left:887px;top:284px;width:85px">Stadt</div>
  <div class="abs select" style="left:991px;top:284px;width:85px">Land</div>
  <div class="abs select" style="left:1094px;top:284px;width:85px">PLZ</div>
  <div class="abs select" style="left:887px;top:326px;width:292px">Wähle Status</div>
  <div class="abs select" style="left:887px;top:368px;width:135px">Preis ab</div>
  <div class="abs select" style="left:1044px;top:368px;width:135px">Preis bis</div>
  <div class="abs btn btn-search">Suche</div>

  <h2 class="abs serif section-title" style="left:70px;top:529px;font-weight:400">Neueste Angebote</h2>
  <div class="abs serif all">Alle zeigen</div>
  <div class="abs arrows">
    <span><svg width="8" height="10"><path d="M6 1 2 5l4 4" stroke="#fff" stroke-width="2" fill="none"/></svg></span>
    <span><svg width="8" height="10"><path d="M2 1l4 4-4 4" stroke="#fff" stroke-width="2" fill="none"/></svg></span>
  </div>

  <article class="abs card" style="left:69px">
    <div class="photo" role="img" aria-label="Foto eines Einfamilienhauses mit Garage" style="background:linear-gradient(180deg,#3f73c4 0%,#9fbbe0 45%,#d8d6c8 60%,#8a9a6a 100%)"></div>
    <div class="tag">Kaufen</div>
    <div class="addr">LINDENSTRASSE 12, 50670 KÖLN</div>
    <div class="row" style="top:240px"><b>Zimmer:</b></div>
    <div class="row" style="top:270px"><b>Bäder:</b><i style="top:-2px">4</i></div>
    <div class="row" style="top:300px"><i style="top:0">2</i></div>
  </article>
  <article class="abs card" style="left:463px">
    <div class="photo" role="img" aria-label="Grundriss einer Wohnung" style="background:linear-gradient(180deg,#fafafa,#e9e9e9)"></div>
    <div class="tag">Mieten</div>
    <div class="addr">GARTENWEG 3B, 70173 STUTTGART</div>
    <div class="row" style="top:240px"><b>Zimmer:</b></div>
    <div class="row" style="top:270px"><b>Bäder:</b><i style="top:-2px">4</i></div>
    <div class="row" style="top:300px"><i style="top:0">2</i></div>
  </article>
  <article class="abs card" style="left:857px">
    <div class="photo" role="img" aria-label="Foto eines weißen Landhauses mit Garten" style="background:linear-gradient(180deg,#4f7fbf 0%,#a7c0dc 35%,#e9ecea 55%,#5c8a34 85%,#3f6e22 100%)"></div>
    <div class="tag">Vermitteln</div>
    <div class="addr">ROSENWEG 7, 22085 HAMBURG</div>
    <div class="row" style="top:240px"><b>Zimmer:</b></div>
    <div class="row" style="top:270px"><b>Bäder:</b><i style="top:-2px">4</i></div>
    <div class="row" style="top:300px"><i style="top:0">2</i></div>
  </article>

  <section class="abs cta">
    <div class="serif headline">LUMAR ist die beste Lösung, wenn es um Ihre Immobilie geht</div>
    <div class="sub">Cras venenatis pellentesque tempus suspendisse vulputate venenatis tristique libero</div>
    <div class="btn">Info anfordern!</div>
  </section>

  <h2 class="abs serif section-title" style="left:70px;top:1051px;font-weight:400">Unser Team</h2>
  <div class="abs member" style="left:69px">
    <div class="photo" role="img" aria-label="Porträtfoto einer Teamperson" style="background:linear-gradient(180deg,#f2f2f2,#a9bcd3)"></div>
    <div class="name">Lena Hofer</div><div class="serif link">Mein Profil zeigen »</div>
  </div>
  <div class="abs member" style="left:267px">
    <div class="photo" role="img" aria-label="Porträtfoto einer Teamperson" style="background:linear-gradient(180deg,#eef1f3,#c9d4e3)"></div>
    <div class="name">Carla Wendt</div><div class="serif link">Mein Profil zeigen »</div>
  </div>
  <div class="abs member" style="left:463px">
    <div class="photo" role="img" aria-label="Porträtfoto einer Teamperson" style="background:linear-gradient(180deg,#e8ecee,#3d4a66)"></div>
    <div class="name">Jonas Keller</div><div class="serif link">Mein Profil zeigen »</div>
  </div>
  <div class="abs member" style="left:659px">
    <div class="photo" role="img" aria-label="Porträtfoto einer Teamperson" style="background:linear-gradient(180deg,#e6ece0,#b9bcc3)"></div>
    <div class="name">Vera Lindner</div><div class="serif link">Mein Profil zeigen »</div>
  </div>
  <ul class="abs bullets">
    <li>Lorem ipsum dolor sit amet, consectetur adipiscing</li>
    <li>Duis suscipit venenatis pellentesque tempor libero</li>
    <li>Etiam aliquet aliquam metus in tristique</li>
    <li>Cras venenatis pellentesque venenatis pellentesque</li>
    <li>Vivamus vitae venenatis pellentesque nunc sed nisl</li>
    <li>In tempus venenatis pellentesquetempor</li>
    <li>Suspendisse vulputate venenatis pellentesque quis</li>
  </ul>

  <footer class="abs footer">
    <div class="abs foot-brand">LUMAR GmbH</div>
    <div class="abs foot-slogan">IHR SLOGAN KOMMT HIERHIN</div>
    <p class="abs foot-text">Lorem ipsum dolor sit amet consectetur incididunt ut labore et dolore magna aliqua adipisicing elit seddo eiusmod tempor.</p>

    <div class="abs foot-head" style="left:366px">ADDRESSE</div>
    <div class="abs foot-addr">
      <div><svg width="14" height="16" viewBox="0 0 14 16"><path d="M7 0a6 6 0 0 0-6 6c0 4 6 10 6 10s6-6 6-10a6 6 0 0 0-6-6zm0 8.5A2.5 2.5 0 1 1 7 3.5a2.5 2.5 0 0 1 0 5z" fill="#aaa"/></svg>Am Rheinweg 48<br>9435 Heerbrugg<br>Schweiz</div>
      <div><svg width="14" height="14" viewBox="0 0 14 18"><path d="M3 0 0 2c0 9 5 15 11 16l3-3-3-4-3 2c-2-2-3-4-3-7l3-1z" fill="#aaa"/></svg>0170 5566 820</div>
      <div><svg width="16" height="12" viewBox="0 0 16 12"><path d="M0 0h16v12H0z" fill="#aaa"/><path d="M0 0l8 6 8-6" stroke="#3a3a3a" stroke-width="1.5" fill="none"/></svg>info@lumar-immo.ch</div>
    </div>

    <div class="abs foot-head" style="left:661px">UNTERNEHMEN</div>
    <ul class="abs foot-links">
      <li>Home</li><li>Über uns</li><li>Verkauf</li><li>Vermietung</li><li>Vermittlung</li><li>Finanzierung</li><li>Kontakt</li>
    </ul>

    <div class="abs foot-head" style="left:957px">PRODUKTE</div>
    <div class="abs foot-photo" role="img" aria-label="Foto eines modernen Hauses mit roter Fassade"></div>
  </footer>

</div>
</body>
</html>
```